Need a business card for our overland brand!

We had the logo made and we need a great design for our business card. Use the logo provide or tweak it however you see fit.

Contact Information for Business Card

Name, Title, Telephone, email, website

```html
<!DOCTYPE html>
<html lang="en">
<head>
<meta charset="utf-8">
<title>Ridgeline Overland — Business Card</title>
<link rel="stylesheet" href="https://fonts.googleapis.com/css2?family=Cabin:wght@400;600;700&display=swap">
<style>
  :root {
    --sky: #1a9bbd;
    --navy: #22354f;
    --snow: #ffffff;
    --stage: #eceeef;
    --card-w: 640px;
    --card-h: 366px;
  }
  * { box-sizing: border-box; margin: 0; padding: 0; }
  html, body {
    width: 1200px; height: 900px; overflow: hidden;
    background: var(--stage);
    font-family: "Cabin", "Gill Sans", sans-serif;
  }
  .stage { position: relative; width: 1200px; height: 900px; }

  .card {
    position: absolute;
    width: var(--card-w); height: var(--card-h);
    background: var(--snow);
    overflow: hidden;
    box-shadow: 0 10px 28px rgba(20, 30, 45, 0.18);
  }
  .card-front { left: 70px; top: 70px; }
  .card-back  { left: 490px; top: 464px; }

  .ridge-art { position: absolute; inset: 0; width: 100%; height: 100%; }

  .front-url {
    position: absolute; right: 70px; top: 40px;
    color: var(--navy); font-size: 13px; font-weight: 700;
    letter-spacing: 3.5px;
  }

  .wordmark {
    position: absolute;
    color: var(--navy); font-weight: 700;
    text-transform: uppercase; line-height: 0.92;
    letter-spacing: -0.5px;
  }
  .card-front .wordmark { left: 150px; top: 200px; font-size: 58px; }
  .card-back .wordmark { right: 34px; top: 30px; font-size: 38px; text-align: right; }

  .contact {
    position: absolute; left: 160px; bottom: 26px;
    display: flex; align-items: flex-start; gap: 18px;
    color: var(--snow);
  }
  .person-name { color: var(--sky); font-weight: 700; font-size: 16px; letter-spacing: 0.5px; line-height: 1.2; }
  .person-title { font-size: 13px; margin-bottom: 8px; line-height: 1.3; }
  .contact-list { list-style: none; font-size: 13px; line-height: 1.5; }
  .contact-list li { display: flex; align-items: center; gap: 8px; }
  .contact-list svg { width: 12px; height: 12px; fill: var(--sky); flex: none; }
  .contact-divider { width: 1px; height: 50px; background: var(--sky); margin-top: 2px; }
  .address { font-size: 13px; line-height: 1.45; font-style: normal; }
</style>
</head>
<body>
<main class="stage">

  <section class="card card-front" aria-label="Card front">
    <svg class="ridge-art" viewBox="0 0 640 366" preserveAspectRatio="none" role="img" aria-label="Mountain ridge silhouette against a blue sky">
      <polygon points="0,0 640,0 640,105 150,85 10,366 0,366" fill="var(--sky)"/>
      <polygon points="10,366 150,85 640,105 640,118 160,100 30,366" fill="var(--navy)"/>
    </svg>
    <p class="front-url">www.ridgelineoverland.com</p>
    <h1 class="wordmark">Ridgeline<br>Overland</h1>
  </section>

  <section class="card card-back" aria-label="Card back">
    <svg class="ridge-art" viewBox="0 0 640 366" preserveAspectRatio="none" role="img" aria-label="Dark mountain range silhouette with a blue ridge line">
      <polygon points="0,366 170,150 640,130 640,366" fill="var(--sky)"/>
      <polygon points="22,366 184,166 640,146 640,366" fill="var(--navy)"/>
    </svg>
    <h2 class="wordmark">Ridgeline<br>Overland</h2>

    <div class="contact">
      <div class="contact-main">
        <p class="person-name">JOHN SMITH</p>
        <p class="person-title">Director</p>
        <ul class="contact-list">
          <li>
            <svg viewBox="0 0 24 24" aria-hidden="true"><path d="M6.6 10.8a15.1 15.1 0 0 0 6.6 6.6l2.2-2.2a1 1 0 0 1 1-.25 11.4 11.4 0 0 0 3.6.57 1 1 0 0 1 1 1V20a1 1 0 0 1-1 1A17 17 0 0 1 3 4a1 1 0 0 1 1-1h3.5a1 1 0 0 1 1 1c0 1.25.2 2.45.57 3.57a1 1 0 0 1-.25 1z"/></svg>
            000-000-0000
          </li>
          <li>
            <svg viewBox="0 0 24 24" aria-hidden="true"><path d="M2 5h20v14H2zm2 2v.4l8 5.2 8-5.2V7z"/></svg>
            info@ridgelineoverland.com
          </li>
          <li>
            <svg viewBox="0 0 24 24" aria-hidden="true"><path d="M12 2a10 10 0 1 0 0 20 10 10 0 0 0 0-20zm0 2c.9 1.2 1.6 2.6 2 4h-4c.4-1.4 1.1-2.8 2-4zM4.3 14a8 8 0 0 1 0-4h3.4a16 16 0 0 0 0 4zm.8 2h3c.3 1.3.8 2.5 1.4 3.6A8 8 0 0 1 5.1 16zM8.1 8h-3a8 8 0 0 1 4.4-3.6C8.9 5.5 8.4 6.7 8.1 8zM12 20c-.9-1.2-1.6-2.6-2-4h4c-.4 1.4-1.1 2.8-2 4zm2.3-6H9.7a14 14 0 0 1 0-4h4.6a14 14 0 0 1 0 4zm.2 5.6c.6-1.1 1.1-2.3 1.4-3.6h3a8 8 0 0 1-4.4 3.6zm1.8-5.6a16 16 0 0 0 0-4h3.4a8 8 0 0 1 0 4zm-.4-6c-.3-1.3-.8-2.5-1.4-3.6A8 8 0 0 1 18.9 8z"/></svg>
            www.ridgelineoverland.com
          </li>
        </ul>
      </div>
      <span class="contact-divider" aria-hidden="true"></span>
      <address class="address">00 dummy city<br>dummy place 0000</address>
    </div>
  </section>

</main>
</body>
</html>
```